Whispers From Distant Stars Poster

So Last year One of the Great Designers from here Came up with a poster for my Events... But Now it is Time to freshen it up.. I have attached the original poster.. I would like the Same wording.. Same Picture of me,. Just fresh Design and colours for the new event year ahead.
This Poster Will be used in Theatres and Hall to Advertise our Event so it needs to stand out but still remain classy
I would Also need The Final Version to be delivered in PhotoShop Version so That I Can Alter Things like the Venue Name, Date, and Ticket Details,, As they change all the time.
Events

```html
<!DOCTYPE html>
<html lang="en">
<head>
<meta charset="utf-8">
<title>Whispers From Distant Stars – An Evening of Mediumship</title>
<link href="https://fonts.googleapis.com/css2?family=Cinzel+Decorative:wght@400;700&family=Raleway:wght@400;500&display=swap" rel="stylesheet">
<style>
  :root {
    --mist-deep: #1c3a44;
    --mist-mid: #4f7c86;
    --mist-pale: #a9cfd2;
    --glow: #f4fff9;
    --title-ink: #1b2e38;
    --title-edge: #e9f6f4;
    --text-light: #eef7ef;
    --skin-tone: #d2ab98;
    --shirt-tone: #dfeef0;
    --suit-tone: #1e2a3a;
  }
  html, body {
    margin: 0;
    padding: 0;
    width: 848px;
    height: 1200px;
    overflow: hidden;
    background: var(--mist-deep);
  }
  .poster {
    position: relative;
    width: 848px;
    height: 1200px;
    overflow: hidden;
    font-family: "Raleway", sans-serif;
  }
  .backdrop {
    position: absolute;
    inset: 0;
    background:
      radial-gradient(ellipse 130px 240px at 270px 470px, var(--glow) 0%, rgba(220,245,240,0.7) 40%, rgba(140,190,195,0) 100%),
      radial-gradient(ellipse 460px 620px at 330px 470px, rgba(169,207,210,0.8) 0%, rgba(79,124,134,0.35) 60%, rgba(28,58,68,0) 100%),
      linear-gradient(90deg, var(--mist-deep) 0%, var(--mist-mid) 30%, var(--mist-mid) 65%, var(--mist-deep) 100%);
  }
  .portrait {
    position: absolute;
    left: 320px;
    top: 228px;
    width: 528px;
    height: 972px;
    border-radius: 230px 230px 0 60px;
    background:
      radial-gradient(ellipse 150px 190px at 145px 180px, var(--skin-tone) 0%, rgba(210,171,152,0.85) 55%, rgba(210,171,152,0) 100%),
      radial-gradient(ellipse 90px 260px at 130px 620px, var(--shirt-tone) 0%, rgba(223,238,240,0) 100%),
      radial-gradient(ellipse 80px 90px at 440px 520px, rgba(210,150,130,0.9) 0%, rgba(210,150,130,0) 100%),
      linear-gradient(180deg, rgba(70,95,110,0.55) 0%, var(--suit-tone) 45%, var(--suit-tone) 85%, rgba(30,42,58,0.6) 100%);
    box-shadow: 0 0 40px 10px rgba(28,58,68,0.35);
  }
  .title {
    position: absolute;
    top: 30px;
    left: 0;
    width: 100%;
    margin: 0;
    text-align: center;
    font-family: "Cinzel Decorative", serif;
    font-weight: 700;
    color: var(--title-ink);
    text-shadow: 0 0 2px var(--title-edge), 0 0 1px var(--title-edge);
    line-height: 1;
  }
  .title-line-one {
    display: block;
    font-size: 70px;
  }
  .title-line-two {
    display: block;
    margin-top: 20px;
    font-size: 54px;
  }
  .tagline {
    position: absolute;
    top: 188px;
    left: 0;
    width: 100%;
    margin: 0;
    text-align: center;
    font-size: 22px;
    letter-spacing: 6px;
    color: var(--title-ink);
  }
  .billing {
    position: absolute;
    left: 0;
    top: 952px;
    width: 870px;
    text-align: center;
    color: var(--text-light);
    text-shadow: 0 1px 4px rgba(10,25,32,0.7);
  }
  .billing p { margin: 0; }
  .billing-role {
    font-size: 23px;
    font-weight: 500;
    letter-spacing: 1px;
  }
  .billing-name {
    font-size: 66px;
    font-weight: 400;
    letter-spacing: 1px;
    line-height: 1;
    margin-top: 2px !important;
  }
  .billing-date {
    font-size: 31px;
    margin-top: 6px !important;
  }
  .billing-venue {
    font-size: 23px;
    font-weight: 500;
    margin-top: 10px !important;
  }
  .billing-tickets {
    font-size: 18px;
    letter-spacing: 1px;
    margin-top: 4px !important;
  }
</style>
</head>
<body>
  <main class="poster">
    <div class="backdrop" role="img" aria-label="Misty teal background with a bright glow of light behind the medium"></div>
    <div class="portrait" role="img" aria-label="Photograph of the medium in a dark suit and open white shirt, reaching a hand toward the viewer"></div>

    <h1 class="title">
      <span class="title-line-one">Whispers From</span>
      <span class="title-line-two">Distant Stars</span>
    </h1>
    <p class="tagline">AN EVENING OF MEDIUMSHIP</p>

    <section class="billing">
      <p class="billing-role">RENOWNED SPIRITUALIST MEDIUM</p>
      <p class="billing-name">OWEN CARROW</p>
      <p class="billing-date">MON 21ST NOV</p>
      <p class="billing-venue">MERIDIAN THEATRE BRACKWELL</p>
      <p class="billing-tickets">For tickets call box office 0170459127</p>
    </section>
  </main>
</body>
</html>
```